Financial Advisor Graphic to Explain Proprietary and Differentiating Investment Strategy

We need a graphic that visualizes how we build a portfolio based on factors of the underlying companies. We use 8 main factors to objectively build an investment porftolio. Our colors are blues, greys (see www.pltvexgroup.com). We are thinking either a venn diagram approach or an atom approach with the factors around the middle "Core Portfolio". This is what differentiates us from everyone in the industry. This will be the key to all of our marketing

Target Market(s)

High net worth investors

Industry/Entity Type

Financial Service

Font styles to use
Serif

Requirements
Must have
• Graphic must be elegant. It is for the financial industry. It should include the following factors (in no order) to build a "Core Portfolio"
• -Counter Cyclical Industries
• -Industry Rate of Recovery
• -Price To Book
• -Absolute Risk
• -Market Capitalization
• -Liquidity
• -Dividend Yield
• -Buy Back Yield
Nice to have
• We are thinking an atom approach or a venn diagram but we are open to new ideas. It must portray the idea that we OBJECTIVELY apply these factors to stock selection to build a core portfolio for our investors. For color pallets see www.pltvexgroup.com It can go beyond the greys and blues but should not be too loud or playful. It can be high tech as long as it portrays seriousness of the financial markets
Should not have
• Can not be playful.

```html
<!DOCTYPE html>
<html lang="en">
<head>
<meta charset="utf-8">
<title>Core Portfolio Factors</title>
<link rel="stylesheet" href="https://fonts.googleapis.com/css2?family=Montserrat:wght@700;800;900&display=swap">
<style>
  :root {
    --bg-light: #e3e3e3;
    --bg-dark: #d9d9d9;
    --ring-fill: #e6e6e6;
    --connector: #a9a9a9;
    --core: #4aa3c8;
    --dividend: #a9a9a9;
    --buyback: #ffffff;
    --counter: #65b180;
    --recovery: #a4b066;
    --price: #6e81ab;
    --risk: #6c9faa;
    --marketcap: #aa8a6c;
    --liquidity: #6c89ab;
    --ink-light: #ffffff;
    --ink-dark: #111111;
  }
  html, body {
    margin: 0;
    padding: 0;
    width: 1200px;
    height: 1077px;
    overflow: hidden;
  }
  .canvas {
    width: 1200px;
    height: 1077px;
    background: repeating-linear-gradient(125deg, var(--bg-light) 0 92px, var(--bg-dark) 92px 184px);
  }
  .diagram { display: block; }
  .connector { stroke: var(--connector); stroke-width: 3.5; }
  .ring { fill: var(--ring-fill); stroke-width: 4; }
  .label {
    font-family: "Montserrat", sans-serif;
    font-weight: 800;
    font-size: 19px;
    fill: var(--ink-light);
    text-anchor: middle;
  }
  .label--dark { fill: var(--ink-dark); }
  .core-title {
    font-family: "Montserrat", sans-serif;
    font-weight: 900;
    font-size: 50px;
    fill: var(--ink-light);
    text-anchor: middle;
    letter-spacing: 1px;
  }
</style>
</head>
<body>
<div class="canvas">
  <svg class="diagram" width="1200" height="1077" viewBox="0 0 1200 1077" aria-label="Core Portfolio built from eight factors">
    <g class="connectors">
      <line class="connector" x1="602" y1="294" x2="602" y2="353"/>
      <line class="connector" x1="812" y1="368" x2="750" y2="425"/>
      <line class="connector" x1="797" y1="557" x2="854" y2="557"/>
      <line class="connector" x1="737" y1="674" x2="803" y2="729"/>
      <line class="connector" x1="602" y1="733" x2="602" y2="789"/>
      <line class="connector" x1="465" y1="678" x2="403" y2="736"/>
      <line class="connector" x1="346" y1="557" x2="403" y2="557"/>
      <line class="connector" x1="387" y1="367" x2="452" y2="423"/>
    </g>

    <g class="core">
      <circle cx="600" cy="538" r="176" fill="var(--core)"/>
      <text class="core-title" x="597" y="530">CORE</text>
      <text class="core-title" x="601" y="568">PORTFOLIO</text>
    </g>

    <g class="factor factor--dividend">
      <circle class="ring" cx="600" cy="168" r="113" stroke="var(--dividend)"/>
      <circle cx="600" cy="168" r="89" fill="var(--dividend)"/>
      <text class="label label--dark" x="600" y="166">DIVIDEND</text>
      <text class="label label--dark" x="603" y="184">YIELD</text>
    </g>

    <g class="factor factor--buyback">
      <circle class="ring" cx="907" cy="284" r="113" stroke="var(--buyback)"/>
      <circle cx="907" cy="284" r="89" fill="var(--buyback)"/>
      <text class="label label--dark" x="906" y="287">BUY BACK</text>
      <text class="label label--dark" x="909" y="305">YIELD</text>
    </g>

    <g class="factor factor--counter">
      <circle class="ring" cx="985" cy="552" r="113" stroke="var(--counter)"/>
      <circle cx="985" cy="552" r="89" fill="var(--counter)"/>
      <text class="label" x="985" y="540">COUNTER</text>
      <text class="label" x="985" y="561">CYCLICAL</text>
      <text class="label" x="987" y="583">INDUSTRIES</text>
    </g>

    <g class="factor factor--recovery">
      <circle class="ring" cx="899" cy="817" r="113" stroke="var(--recovery)"/>
      <circle cx="899" cy="817" r="89" fill="var(--recovery)"/>
      <text class="label" x="898" y="812">INDUSTRY</text>
      <text class="label" x="898" y="834">RATE OF</text>
      <text class="label" x="900" y="856">RECOVERY</text>
    </g>

    <g class="factor factor--price">
      <circle class="ring" cx="597" cy="922" r="113" stroke="var(--price)"/>
      <circle cx="597" cy="922" r="89" fill="var(--price)"/>
      <text class="label" x="596" y="921">PRICE</text>
      <text class="label" x="598" y="939">TO BOOK</text>
    </g>

    <g class="factor factor--risk">
      <circle class="ring" cx="302" cy="817" r="113" stroke="var(--risk)"/>
      <circle cx="302" cy="817" r="89" fill="var(--risk)"/>
      <text class="label" x="303" y="820">ABSOLUTE</text>
      <text class="label" x="305" y="838">RISK</text>
    </g>

    <g class="factor factor--marketcap">
      <circle class="ring" cx="215" cy="553" r="113" stroke="var(--marketcap)"/>
      <circle cx="215" cy="553" r="89" fill="var(--marketcap)"/>
      <text class="label" x="212" y="557">MARKET</text>
      <text class="label" x="214" y="573">CAPITALIZATION</text>
    </g>

    <g class="factor factor--liquidity">
      <circle class="ring" cx="299" cy="279" r="113" stroke="var(--liquidity)"/>
      <circle cx="299" cy="279" r="89" fill="var(--liquidity)"/>
      <text class="label" x="299" y="289">LIQUIDITY</text>
    </g>
  </svg>
</div>
</body>
</html>
```